Corporate Website for Harbor Signal
Landing Page + Rotating Banner (3) Designs
Thanks to all who took part in this design brief. Your collective creative instincts made it difficult for us to finalize a concept. Congratulations go to tuvelsk42 who for us developed a fitting image for the Harbor Signal web site.
It has been a very rewarding process for us as it has displayed a viable avenue for future web design sourcing and we hope to work with you all again soon.
Kind Regards
Odrey
Ok we've got a few designers still in and most have managed to fulfil the brief requirements with some nice clean layouts a colour combinations. We're just looking for the correct theme/background to accompany the content. If I don't see any development on this by tomorrow, I will extend the project by a few days to give you time to develop your concepts. Remember not too bold, just something to subtly occupy the white space behind the main template.
Thank you for your efforts so far.
Hi Brightfold
I like your subtle use of colour on the menu and how it ties in with the logo. (I have attached our logo to this brief, please apply this to your next draft). Can you try a different colour concept for the top bar behind the logo.
The shadow cast by the page is also a nice touch but for your next draft can we see more reference to the industry as inspiration for the background concept i.e. "digital", "technology", "electronics" etc.(faded, not to prominent).
Can you change the promotional banner to contain just one image concept of your own ( not too complicated, just fill the space with a fitting mood ). Also can you make better use of the space on the lower half of the page.
Thank you for your submission.
Just to clarify to all those wishing to develop for this design brief, we are mainly looking for an elegant sophisticated landing page, the 3 banner designs are secondary to this.
Hi salvemora
The reason I have given a one star rating is based on the brief requirements.
We are looking for a clean professional corporate landing page. We find the use of font size and colour in your submission does not represent our needs. A better use of white space and typography and less emphasis on full colour background would boost your submissions appeal.
Please view the example websites as a guide and also incorporate our logo provided to help with colour concepts.
Thanks again for your entry.

```html
<!DOCTYPE html>
<html lang="en">
<head>
<meta charset="utf-8">
<title>Harbor Signal</title>
<link href="https://fonts.googleapis.com/css2?family=Arimo:wght@400;700&display=swap" rel="stylesheet">
<style>
:root{
  --bg-light:#c9c9c9;
  --bg-mid:#a9a9a9;
  --bg-dark:#5e5e5e;
  --floor:#3c3c3c;
  --panel:#f4f4f4;
  --white:#ffffff;
  --ink:#333333;
  --ink-soft:#666666;
  --nav-ink:#ffffff;
  --brand:#7a3fa0;
  --accent:#7cc242;
  --news-red:#c8102e;
  --banner-dark:#1c1a18;
  --banner-glow:#a85a1c;
  --box-border:#e0e0e0;
}
*{margin:0;padding:0;box-sizing:border-box}
html,body{width:1200px;height:674px;overflow:hidden}
body{
  position:relative;
  font-family:"Arimo",Arial,sans-serif;
  color:var(--ink);
  background:
    radial-gradient(ellipse 520px 360px at 600px 260px,#e2e2e2 0%,rgba(226,226,226,0) 100%),
    linear-gradient(180deg,var(--bg-mid) 0%,var(--bg-light) 35%,var(--bg-mid) 80%,var(--bg-dark) 94%);
}
.floor{position:absolute;left:0;right:0;bottom:0;height:36px;
  background:linear-gradient(180deg,var(--bg-dark),var(--floor))}
.floor::before{content:"";position:absolute;left:0;right:0;top:0;height:6px;background:#7a7a7a}

.site-header{position:absolute;inset:0;z-index:2;pointer-events:none}
.brand{position:absolute;left:352px;top:20px;display:flex;align-items:center;gap:6px}
.brand-mark{width:12px;height:12px;border-radius:50%;background:var(--brand)}
.brand-name{font-size:20px;font-weight:700;color:var(--brand);white-space:nowrap}

.search{position:absolute;left:692px;top:16px;width:160px;height:13px;background:var(--white);
  border-radius:7px;border:1px solid #999}
.search-btn{position:absolute;right:1px;top:1px;width:9px;height:9px;border-radius:50%;background:#4a90c8}

.main-nav{position:absolute;left:512px;top:38px;display:flex}
.main-nav a{display:block;padding:4px 6px;font-size:10px;line-height:12px;color:var(--nav-ink);text-decoration:none;white-space:nowrap}
.main-nav a.active{background:#6f6f6f;border-top:3px solid var(--accent);padding-top:1px}

.tip{position:absolute;top:60px;background:var(--white);border-radius:3px;
  box-shadow:0 1px 4px rgba(0,0,0,.35);font-size:6.5px;line-height:8.5px;color:var(--ink-soft);padding:6px}
.tip-about{left:492px;width:84px;height:50px}
.tip-follow{left:584px;width:76px;height:58px;text-align:center}
.tip-follow h4{font-size:8px;line-height:9px;font-weight:700;color:var(--ink);margin-bottom:4px}
.social{display:grid;grid-template-columns:repeat(2,14px);gap:4px;justify-content:center}
.social span{width:14px;height:14px;background:#555;border-radius:2px}
.tip-ship{left:668px;width:76px;height:50px}

.page{position:absolute;left:293px;top:79px;width:614px;height:564px;background:var(--panel);
  border-radius:8px;box-shadow:0 10px 30px rgba(0,0,0,.35);z-index:1}
.banner{position:absolute;left:5px;top:17px;width:604px;height:187px;
  background:radial-gradient(ellipse 300px 120px at 50% 60%,var(--banner-glow) 0%,var(--banner-dark) 75%)}
.banner-dots{position:absolute;left:300px;top:176px;display:flex;gap:6px}
.banner-dots span{width:6px;height:6px;border-radius:50%;background:#888}
.banner-dots span.on{background:var(--white)}
.news{position:absolute;left:5px;top:206px;width:604px;height:14px;background:var(--white);
  border-bottom:1px solid #ddd;font-size:7px;line-height:14px;color:var(--ink-soft);padding-left:6px;white-space:nowrap;overflow:hidden}
.news b{color:var(--news-red);margin-right:8px}

.feature{position:absolute;height:110px;background:var(--white);
  border:1px solid var(--box-border);box-shadow:0 1px 3px rgba(0,0,0,.12);padding:14px 0 0 10px;
  font-size:9px;line-height:12px;color:var(--ink)}
.feature .shot{position:absolute;right:12px;top:18px;height:72px;border-radius:4px}
.f1{left:67px;top:257px;width:206px}
.f1 p{width:104px}
.f1 .shot{width:70px;background:linear-gradient(135deg,#ffffff,#cfd8df)}
.f2{left:283px;top:257px;width:264px}
.f2 p{width:112px}
.f2 .shot{width:92px;background:linear-gradient(135deg,#e8e8e8,#3a3a3a)}
.f3{left:67px;top:389px;width:206px}
.f3 p{width:104px}
.f3 .shot{width:60px;background:linear-gradient(135deg,#f2f2f2,#9aa7b3)}
.f4{left:283px;top:389px;width:264px}
.f4 p{width:128px}
.f4 .shot{width:98px;background:linear-gradient(135deg,#b9c4d0,#222222)}
</style>
</head>
<body>
<div class="floor"></div>

<header class="site-header">
  <div class="brand"><span class="brand-mark"></span><span class="brand-name">Harbor Signal</span></div>
  <div class="search"><span class="search-btn"></span></div>
  <nav class="main-nav">
    <a class="active" href="#">ABOUT</a>
    <a href="#">PRODUCTS</a>
    <a href="#">PRESS</a>
    <a href="#">CONTACT</a>
    <a href="#">WHERE TO BUY</a>
    <a href="#">FOLLOW US</a>
  </nav>
  <div class="tip tip-about">Learn who we are, what we build and where we are going next.</div>
  <div class="tip tip-follow"><h4>Follow Us</h4>
    <div class="social"><span></span><span></span><span></span><span></span></div>
  </div>
  <div class="tip tip-ship">We are now shipping to retail partners across the region.</div>
</header>

<main class="page">
  <div class="banner" role="img" aria-label="Promotional banner with three product offers on a dark amber background"></div>
  <div class="banner-dots"><span class="on"></span><span></span><span></span></div>
  <div class="news"><b>NEWS</b>We are now shipping our latest range to partners across the region, with new devices in stock this month</div>

  <section class="feature f1">
    <p>Mobile Broadband Computing is a superb alternative for UK internet users to fixed broadband via telephone line connec-</p>
    <div class="shot" role="img" aria-label="White mobile broadband dongle"></div>
  </section>
  <section class="feature f2">
    <p>Kestrel Labs' Peripherals range provides products designed to add convenience for users.</p>
    <div class="shot" role="img" aria-label="Small peripheral devices and cables"></div>
  </section>
  <section class="feature f3">
    <p>Kestrel Labs Ltd offers a range of cutting edge Data Recovery products that meet for reaching surveillance needs.</p>
    <div class="shot" role="img" aria-label="Data recovery USB stick"></div>
  </section>
  <section class="feature f4">
    <p>This Linkwave keyboard has been especially designed for the Slate &amp; Slate 2 (with aperture for digital camera) but is also compatible with Orbis and Tarn.</p>
    <div class="shot" role="img" aria-label="Tablet in a keyboard case"></div>
  </section>
</main>
</body>
</html>
```